Visitenkarten-Design für Familienunternehmen (Apotheke)
Zielgruppe
Wir sind ein Familienunternehmen und betreiben 4 Apotheken (alle eigene Namen: Lindenhain-Apotheke; Quellen-Apotheke; Apotheke Am Brunnentor und Vitalora-Apotheke)
Wir beginnen, diese alle unter Eulen-Apotheken zusammenzufassen. www.eulen-apotheken.de (die Vitalora-Apotheke eröffnet erst am 1.1.18 neu, daher noch nicht online)
Konkret möchten wir für die Mitarbeiter der Vitalora-Apotheke Visitenkarten mit Porträt für Kunden erstellen.
Aktuell sind wir ca. 10 Mitarbeiter in dieser Apotheke. Ggf. möchten wir mittelfristig alle Mitarbeiter aller Apotheken (ca. 50-60) mit Visitenkarten ausstatten.
Aufgabenstellung
Wir haben vor Jahren selbst laienhaft eine Visitenkarte erstellt
Ich habe gegoogelt und andere Beispiele mit Porträt gefunden.
Wir suchen eine Visitenkarte, die sowohl das Logo Vitalora-Apotheke inkl. Adresse, Telefonnummer etc. hat (kann auch optisch verschoben werden - oben Logo - unten Adresse o.ä) , den Namen des Mitarbeitern und Beruf (Apothekerin o.ä.) und 2-3 Schlagwörter/Schlagsätze zu der Qualifikation des Mitarbeiters.
(die Vitalora-Apotheke hat eine Spezialzertifizierung 'Wiegensichere Offizin' und darf daher auch das Logo Wiegensichere Offizin nutzen. Eventuell gibt es die Möglichkeit dieses auch - nicht konkurrierend - neben dem Hauptlogo Vitalora-Apotheke unterzubringen)
unten gerne 'Eulen-Apotheken' o.ä. als Dachmarke
Mutter-Kind-Expertin (Zertifizierung Wiegensichere Offizin)
Fachberaterin für Darmgesundheit
!! Seriös, weniger verspielt. Druckbar für Druckwerkel, wir nehmen gerne Tipps zu Papier und Stärke an!
Ziel: Klares Design, wo einfach der Kopf des Mitarbeiters gewechselt werden kann und die Qualifikation, um für alle Mitarbeiter gleiche CI zu erstellen

```html
<!DOCTYPE html>
<html lang="de">
<head>
<meta charset="utf-8">
<title>Visitenkarte Vitalora-Apotheke</title>
<link rel="stylesheet" href="https://fonts.googleapis.com/css2?family=Roboto:wght@300;400;700;900&display=swap">
<style>
  :root {
    --bg: #ebebeb;
    --card: #ffffff;
    --ink: #231f20;
    --accent: #c8262c;
    --muted: #a3a3a3;
    --photo-light: #d9cfc8;
    --photo-dark: #3a2a22;
  }
  * { box-sizing: border-box; margin: 0; padding: 0; }
  html, body {
    width: 1187px; height: 1200px; overflow: hidden;
    background: var(--bg);
    font-family: "Roboto", Arial, sans-serif;
    color: var(--ink);
  }
  .stage {
    position: relative; width: 1187px; height: 1200px;
    display: flex; align-items: center; justify-content: center; gap: 40px;
  }
  .card {
    position: relative; width: 520px; height: 337px;
    background: var(--card);
    box-shadow: 0 2px 8px rgba(0,0,0,.18);
  }
  /* front */
  .portrait {
    position: absolute; left: 0; bottom: 0; width: 230px; height: 337px;
    background: linear-gradient(180deg, var(--photo-light) 0%, #b89a88 40%, var(--photo-dark) 100%);
  }
  .badge { position: absolute; right: 20px; top: 18px; }
  .person { position: absolute; left: 258px; top: 118px; }
  .person-name { color: var(--accent); font-size: 20px; font-weight: 400; }
  .person-role { font-size: 13px; margin-top: 8px; }
  .qualifications {
    margin-top: 26px; color: var(--muted); font-size: 11.5px; font-weight: 300; line-height: 1.45;
  }
  .logo-small {
    position: absolute; right: 34px; bottom: 26px;
    display: flex; align-items: center; gap: 6px;
    font-size: 16px; font-weight: 700; color: var(--ink);
  }
  .dot { display: inline-block; border-radius: 50%; background: var(--accent); }
  .logo-small .dot { width: 10px; height: 10px; }
  /* back */
  .back { display: flex; flex-direction: column; align-items: center; }
  .logo-large {
    margin-top: 88px;
    display: flex; align-items: center; gap: 12px;
    font-size: 36px; font-weight: 900; color: var(--ink); letter-spacing: -0.5px;
  }
  .logo-large .dot { width: 22px; height: 22px; }
  .address { margin-top: 44px; font-size: 16px; font-weight: 400; }
  .address .sep { margin: 0 14px; }
  .contact { margin-top: 24px; font-size: 12.5px; line-height: 1.45; text-align: center; }
</style>
</head>
<body>
<main class="stage">
  <section class="card front">
    <div class="portrait" role="img" aria-label="Porträtfoto der Mitarbeiterin"></div>
    <svg class="badge" width="96" height="40" viewBox="0 0 96 40" aria-hidden="true">
      <ellipse cx="48" cy="20" rx="45" ry="17" fill="none" stroke="#c8262c" stroke-width="2"/>
    </svg>
    <div class="person">
      <h1 class="person-name">Johanna Veltrup</h1>
      <p class="person-role">Apothekerin</p>
      <p class="qualifications">
        Mutter-Kind-Expertin<br>
        (Zertifizierung Wiegensichere Offizin)<br>
        Fachberaterin für Darmgesundheit
      </p>
    </div>
    <div class="logo-small"><span>Vitalora-Apotheke</span><span class="dot"></span></div>
  </section>

  <section class="card back">
    <div class="logo-large"><span>Vitalora-Apotheke</span><span class="dot"></span></div>
    <p class="address">Kesselgasse 22<span class="sep">|</span>92318 Neumarkt</p>
    <p class="contact">
      tel: 09181 / 438260-0&nbsp;&nbsp;&nbsp;fax: 09181 / 438260-1<br>
      vitalora@eulen-apotheken.de<br>
      www.eulen-apotheken.de
    </p>
  </section>
</main>
</body>
</html>
```